Business Card for Inovative Flexible Packaging Company

Create a business card that is both simple and stricking at the same time.
Preferably only one color (orange) or two colors (black and orange).
Information to print:
Torvalo, Lda
[T] 22 418 6093
[M] 91 326 7041
[F] 22 418 6135
[@] torvalo.ac@correiomx.com
SEDE & ENTREPOSTO
Rua Das Figueiras do Monte, 312
Valdoura
4410-832 Valdoura - VN Ribamar
PORTUGAL
Reason: A lot of the ideas are obvious. I want something different. Inovative. dare to do something eye catching with style.
Business Consumers. Packaging Designers.
Business

```html
<!DOCTYPE html>
<html lang="pt">
<head>
<meta charset="utf-8">
<title>Torvalo — Business Card</title>
<link rel="stylesheet" href="https://fonts.googleapis.com/css2?family=Mulish:wght@400;600;800&display=swap">
<style>
  :root {
    --orange: #ef7f2e;
    --orange-deep: #f26a10;
    --ink: #3a3a3a;
    --paper: #ffffff;
    --backdrop: #e9e7e4;
  }
  * { box-sizing: border-box; margin: 0; padding: 0; }
  html, body {
    width: 1200px; height: 1000px; overflow: hidden;
    background: var(--backdrop);
    font-family: "Mulish", Arial, sans-serif;
  }
  .sheet {
    position: relative; width: 1200px; height: 1000px;
    display: flex; flex-direction: column; align-items: center;
    justify-content: center; gap: 60px;
  }
  .card {
    position: relative; width: 720px; height: 420px;
    background: var(--paper);
    box-shadow: 0 6px 18px rgba(0,0,0,0.18);
    overflow: hidden;
  }
  .card__shapes { position: absolute; inset: 0; width: 100%; height: 100%; }
  .brand { position: absolute; display: flex; align-items: center; gap: 22px; }
  .brand__mark { width: 92px; height: 92px; background: var(--orange-deep); flex: none; }
  .brand__text { display: flex; flex-direction: column; }
  .brand__name {
    font-weight: 800; font-size: 96px; line-height: 0.9;
    color: var(--orange-deep); letter-spacing: -2px;
  }
  .brand__tagline {
    font-weight: 600; font-size: 15px; letter-spacing: 6px;
    color: var(--ink); margin-top: 10px; text-transform: uppercase;
  }
  .card--front .brand { left: 70px; top: 150px; }
  .card--back .brand { left: 60px; top: 50px; }
  .card--back .brand__name { font-size: 86px; }
  .card--back .brand__mark { width: 84px; height: 84px; }

  .address {
    position: absolute; left: 70px; top: 248px;
    padding-left: 22px; border-left: 3px solid var(--orange);
    color: var(--ink); font-size: 14px; line-height: 1.45; font-style: normal;
  }
  .address__company { margin-bottom: 14px; }
  .contacts {
    position: absolute; left: 392px; top: 238px;
    list-style: none; color: var(--ink); font-size: 15px;
  }
  .contacts__item { display: flex; align-items: center; gap: 12px; height: 34px; }
  .contacts__icon { width: 26px; height: 26px; flex: none; }
</style>
</head>
<body>
<main class="sheet">

  <section class="card card--front" aria-label="Card front">
    <svg class="card__shapes" viewBox="0 0 720 420" aria-hidden="true">
      <polygon points="0,0 230,0 0,90" fill="var(--orange)"/>
      <polygon points="0,420 0,395 310,350 300,420" fill="var(--orange)"/>
      <polygon points="615,0 720,0 720,420 705,420 580,215" fill="var(--orange)"/>
    </svg>
    <div class="brand">
      <div class="brand__mark"></div>
      <div class="brand__text">
        <span class="brand__name">torvalo</span>
        <span class="brand__tagline">Flexible Wrapping</span>
      </div>
    </div>
  </section>

  <section class="card card--back" aria-label="Card back">
    <svg class="card__shapes" viewBox="0 0 720 420" aria-hidden="true">
      <polygon points="695,0 720,0 720,420 668,420" fill="var(--orange)"/>
    </svg>
    <div class="brand">
      <div class="brand__mark"></div>
      <div class="brand__text">
        <span class="brand__name">torvalo</span>
        <span class="brand__tagline">Flexible Wrapping</span>
      </div>
    </div>

    <address class="address">
      <p class="address__company">Torvalo, Lda</p>
      <p>SEDE &amp; ENTREPOSTO</p>
      <p>Rua Das Figueiras do Monte, 312</p>
      <p>Valdoura</p>
      <p>4410-832 Valdoura - VN Ribamar</p>
      <p>PORTUGAL</p>
    </address>

    <ul class="contacts">
      <li class="contacts__item">
        <svg class="contacts__icon" viewBox="0 0 26 26" aria-label="Telefone"><circle cx="13" cy="13" r="13" fill="var(--orange)"/><path d="M8 7.5l3 0 1 3.5-1.8 1.2a8 8 0 0 0 3.6 3.6L15 14l3.5 1v3c-6 .5-11-4.5-10.5-10.5z" fill="#fff"/></svg>
        <span>22 418 6093</span>
      </li>
      <li class="contacts__item">
        <svg class="contacts__icon" viewBox="0 0 26 26" aria-label="Telemóvel"><circle cx="13" cy="13" r="13" fill="var(--orange)"/><rect x="9" y="6" width="8" height="14" rx="1.5" fill="#fff"/><rect x="10.5" y="8" width="5" height="9" fill="var(--orange)"/></svg>
        <span>91 326 7041</span>
      </li>
      <li class="contacts__item">
        <svg class="contacts__icon" viewBox="0 0 26 26" aria-label="Fax"><circle cx="13" cy="13" r="13" fill="var(--orange)"/><rect x="9" y="6" width="8" height="5" fill="#fff"/><rect x="6" y="11" width="14" height="8" rx="1" fill="#fff"/><rect x="9" y="13" width="8" height="1.5" fill="var(--orange)"/></svg>
        <span>22 418 6135</span>
      </li>
      <li class="contacts__item">
        <svg class="contacts__icon" viewBox="0 0 26 26" aria-label="Email"><circle cx="13" cy="13" r="13" fill="var(--orange)"/><rect x="6.5" y="8.5" width="13" height="9" fill="#fff"/><path d="M6.5 8.5l6.5 5 6.5-5" fill="none" stroke="var(--orange)" stroke-width="1.3"/></svg>
        <span>torvalo.ac@correiomx.com</span>
      </li>
    </ul>
  </section>

</main>
</body>
</html>
```